KVE Palliative Care Flyer

We need an A5 flyer designed for print on high quality card. The flyer will be placed on every seat at two Brindlewood Chamber Ensemble concerts dedicated to awareness raising of palliative care. We would like to have a flyer that uses our logo, and an image of a couple waltzing or in waltz hold. The final design should communicate the essence of palliative care which is that you matter to us, and you matter right to the very end of your life. "Putting life in the days, not days in the life".

Target Market(s)

Concert goers

Requirements
Must have
• Gentle Harbour Alliance SA logo

```html
<!DOCTYPE html>
<html lang="en">
<head>
<meta charset="utf-8">
<title>KVE Palliative Care Flyer</title>
<link rel="stylesheet" href="https://fonts.googleapis.com/css2?family=Questrial&family=Open+Sans:wght@700;800&display=swap">
<style>
  :root {
    --page-bg: #e9e7e3;
    --card-white: #ffffff;
    --card-grey-top: #f7f7f7;
    --card-grey-bottom: #dcdcdc;
    --aqua: #3ab8dc;
    --aqua-light: #8fdcf0;
    --aqua-pale: #c9eef8;
    --brand-blue: #2a9fd0;
    --panel-grey: #a4a4a4;
    --panel-grey-top: #b0b0b0;
    --text-grey: #5a5a5a;
    --white: #ffffff;
  }
  * { box-sizing: border-box; margin: 0; padding: 0; }
  html, body { width: 1200px; height: 1000px; overflow: hidden; }
  body {
    background: var(--page-bg);
    font-family: "Questrial", "Century Gothic", sans-serif;
    color: var(--text-grey);
    position: relative;
  }
  .flyer {
    position: absolute;
    top: 60px;
    width: 440px;
    height: 880px;
    background: linear-gradient(180deg, var(--card-grey-top) 0%, var(--card-grey-bottom) 100%);
    box-shadow: 0 6px 18px rgba(0,0,0,0.18);
    overflow: hidden;
  }
  .flyer--back { left: 120px; }
  .flyer--front { left: 640px; }

  .flyer__header {
    position: relative;
    height: 110px;
    background: var(--card-white);
  }
  .flyer__header-tab {
    position: absolute;
    right: 0; bottom: 0;
    width: 150px; height: 44px;
    background: linear-gradient(100deg, var(--aqua) 0%, var(--aqua-light) 60%, var(--aqua-pale) 100%);
  }
  .brand {
    position: absolute;
    left: 40px; top: 28px;
    display: flex; align-items: center; gap: 10px;
  }
  .brand__dot {
    width: 22px; height: 22px; border-radius: 50%;
    background: var(--brand-blue);
  }
  .brand__name {
    font-size: 15px; line-height: 1.1;
    color: var(--brand-blue);
    width: 150px;
  }

  .flyer__body {
    padding: 28px 40px 0;
    font-size: 11px;
    line-height: 1.5;
  }
  .flyer__body p { margin-bottom: 10px; }

  .flyer__footer {
    position: absolute;
    left: 0; right: 0; bottom: 0;
    height: 120px;
    background:
      linear-gradient(100deg, rgba(255,255,255,0) 40%, rgba(255,255,255,0.35) 55%, rgba(255,255,255,0) 70%),
      linear-gradient(180deg, var(--aqua) 0%, var(--aqua-light) 70%, var(--aqua-pale) 100%);
  }

  /* back side: contact panel */
  .contact-panel {
    position: absolute;
    left: 30px; right: 30px; bottom: 150px;
    height: 200px;
    border-radius: 14px;
    background: linear-gradient(180deg, #b4b4b4 0%, var(--panel-grey) 100%);
    color: var(--white);
    padding: 22px;
  }
  .contact-panel__name {
    font-family: "Open Sans", sans-serif;
    font-weight: 800;
    font-size: 17px; line-height: 1.25;
    margin-bottom: 14px;
  }
  .contact-panel__grid {
    display: flex; justify-content: space-between;
    font-size: 12px; line-height: 1.55;
  }
  .contact-panel__address { font-style: normal; }

  /* front side: headline bubble and waltz image area */
  .headline-bubble {
    position: absolute;
    z-index: 2;
    left: 30px; top: 150px;
    width: 240px; height: 270px;
    border-radius: 14px;
    background: linear-gradient(180deg, var(--panel-grey-top) 0%, var(--panel-grey) 100%);
    color: var(--white);
    padding: 20px 18px;
  }
  .headline-bubble__tail {
    position: absolute;
    left: 20px; top: -22px;
  }
  .headline-bubble__title {
    font-family: "Open Sans", sans-serif;
    font-weight: 800;
    font-size: 16px; line-height: 1.22;
    margin-bottom: 12px;
  }
  .headline-bubble__note { font-size: 11.5px; line-height: 1.45; }
  .dancers {
    position: absolute;
    z-index: 1;
    left: 255px; top: 170px;
    width: 165px; height: 250px;
    background: linear-gradient(180deg, #f2f2f2 0%, #cfcfcf 100%);
    border-radius: 4px;
  }
  .flyer--front .flyer__body { padding-top: 340px; }
</style>
</head>
<body>

  <section class="flyer flyer--back">
    <header class="flyer__header">
      <div class="brand">
        <span class="brand__dot"></span>
        <span class="brand__name">Gentle Harbour Alliance SA</span>
      </div>
      <div class="flyer__header-tab"></div>
    </header>
    <div class="flyer__body">
      <p>Just as everyone can learn to waltz, everyone should be prepared to consider the circumstances of major illness and the threat of dying – we never know its timing.</p>
      <p>And we should be prepared to start a conversation with those close to us about how we wish a serious illness to be managed. It will serve to dispel anxieties and fears and will facilitate communication in crisis situations. South Australia is preparing Advance Care Directives legislation that will encourage us all to do this, and write it down.</p>
      <p>Tonight we affirm both the spirit-lifting rhythm of the waltz, and the heart warming work of palliative care.</p>
      <p>Everyone should understand also what palliative care can offer to make the ‘dance with death’ something not to be feared. It is not about helping to die, more about ensuring comfort and fostering patience, courage and love. These are the values of life itself. The Gentle Harbour Alliance will welcome your queries and assistance.</p>
    </div>
    <div class="contact-panel">
      <h2 class="contact-panel__name">Gentle Harbour Alliance<br>South Australia Inc</h2>
      <div class="contact-panel__grid">
        <address class="contact-panel__address">
          Suite 4 18-22 Wattlebird Lane<br>
          Eastwood SA 5071<br>
          PO Box 219 Eastwood SA 5071
        </address>
        <div class="contact-panel__details">
          P: 8340 2957<br>
          E: hello@gentleharbour.org.au<br>
          W: www.gentleharbour.org.au
        </div>
      </div>
    </div>
    <footer class="flyer__footer"></footer>
  </section>

  <section class="flyer flyer--front">
    <header class="flyer__header">
      <div class="brand">
        <span class="brand__dot"></span>
        <span class="brand__name">Gentle Harbour Alliance SA</span>
      </div>
      <div class="flyer__header-tab"></div>
    </header>

    <div class="headline-bubble">
      <svg class="headline-bubble__tail" width="40" height="24" viewBox="0 0 40 24" aria-hidden="true">
        <polygon points="0,0 40,24 8,24" fill="#b0b0b0"/>
      </svg>
      <h1 class="headline-bubble__title">What does the VIENNESE WALTZ have to do with Palliative Care?</h1>
      <p class="headline-bubble__note">The Gentle Harbour Alliance South Australia Inc is grateful to the Brindlewood Chamber Ensemble for its welcome to this partnership concert.</p>
    </div>
    <div class="dancers" role="img" aria-label="Illustration of a couple dancing in waltz hold"></div>

    <div class="flyer__body">
      <p>It may seem strange that the energy and life of the Viennese waltz could be linked with the situation of those who have advanced and terminal illness.</p>
      <p>The waltz is a smooth and progressive dance for a ballroom or folk-gathering; it calls for partnership, expertise and the assistance of music, best offered by a team of instrumentalists, none better that our KVE.</p>
      <p>Palliative care also seeks to be smooth and progressive in its offer of care – always available, responsive, and in partnership with the patient and family. It calls for medical and nursing expertise, but just as each waltzing couple has its own individual style, palliative care seeks to be patient-centred, offering the support that the patient and family see as most appropriate for them.</p>
      <p>Some persons feel they cannot dance; many feel unable to approach the prospect of death and dying.</p>
    </div>
    <footer class="flyer__footer"></footer>
  </section>

</body>
</html>
```